Orva Business Card

we need a business card for flooring business called Orva Flooring, the design should be black and white. we have 2 locations

Harwood Showroom
527 Kellerman Road,
Harwood VIC 3142

Linfield Showroom
462 Bramwell Hwy,
Linfield VIC 3218

email : sales@orvaflooring.com.au
(03) 9471 2830

Please inform we sell , Laminate, Hybrid, Timber, carpet and commercial flooring

```html
<!DOCTYPE html>
<html lang="en">
<head>
<meta charset="utf-8">
<title>Orva Flooring Business Card</title>
<link rel="stylesheet" href="https://fonts.googleapis.com/css2?family=Montserrat:wght@400;500;700&display=swap">
<style>
  :root {
    --backdrop: #e4e4e4;
    --card: #ffffff;
    --ink: #1b1b1b;
    --rule: #2a2a2a;
  }
  * { margin: 0; padding: 0; box-sizing: border-box; }
  html, body {
    width: 1093px; height: 1200px; overflow: hidden;
    background: var(--backdrop);
    font-family: "Montserrat", Arial, sans-serif;
    color: var(--ink);
  }
  .canvas { position: relative; width: 1093px; height: 1200px; }
  .card {
    position: absolute;
    background: var(--card);
    border-radius: 16px;
  }
  .card--front { left: 265px; top: 225px; width: 580px; height: 363px; }
  .card--back  { left: 259px; top: 616px; width: 595px; height: 366px; }

  .person { position: absolute; left: 31px; top: 45px; }
  .person__name { font-size: 21px; font-weight: 700; letter-spacing: 0.2px; line-height: 1.2; }
  .person__title { font-size: 12.5px; font-weight: 500; margin-top: 1px; }

  .wordmark {
    position: absolute;
    display: flex; align-items: center; gap: 10px;
    font-weight: 500; color: var(--ink);
  }
  .wordmark__dot { width: 14px; height: 14px; border-radius: 50%; background: var(--ink); flex: none; }
  .wordmark__text { line-height: 1; white-space: nowrap; }
  .card--front .wordmark { right: 24px; top: 82px; font-size: 31px; }
  .card--back .wordmark { left: 0; right: 0; top: 122px; justify-content: center; font-size: 38px; }

  .address { position: absolute; font-size: 12.5px; line-height: 17.5px; font-weight: 500; font-style: normal; }
  .address--harwood { left: 28px; top: 207px; }
  .address--linfield { left: 403px; top: 284px; }

  .contacts { position: absolute; left: 28px; top: 282px; list-style: none; font-size: 12.8px; font-weight: 500; }
  .contacts li { display: flex; align-items: center; gap: 6px; height: 20px; }
  .contacts svg { width: 12px; height: 12px; fill: var(--ink); flex: none; }

  .services { position: absolute; left: 0; right: 0; top: 272px; text-align: center; }
  .services__heading {
    display: inline-block; font-size: 17px; font-weight: 700;
    padding: 0 4px 3px; border-bottom: 1.5px solid var(--rule);
  }
  .services__list { margin-top: 18px; font-size: 16px; font-weight: 500; }
</style>
</head>
<body>
<main class="canvas">
  <section class="card card--front">
    <div class="person">
      <p class="person__name">Nadia Carrow</p>
      <p class="person__title">Managing Director</p>
    </div>

    <div class="wordmark">
      <span class="wordmark__dot"></span>
      <span class="wordmark__text">Orva Flooring</span>
    </div>

    <address class="address address--harwood">
      Harwood Showroom<br>527 Kellerman Road,<br>Harwood VIC 3142
    </address>

    <ul class="contacts">
      <li><svg viewBox="0 0 24 24"><path d="M6.6 10.8a15.1 15.1 0 0 0 6.6 6.6l2.2-2.2a1 1 0 0 1 1-.25 11.4 11.4 0 0 0 3.6.57 1 1 0 0 1 1 1V20a1 1 0 0 1-1 1A17 17 0 0 1 3 4a1 1 0 0 1 1-1h3.5a1 1 0 0 1 1 1c0 1.25.2 2.45.57 3.6a1 1 0 0 1-.25 1z"/></svg>(03) 9471 2830</li>
      <li><svg viewBox="0 0 24 24"><path d="M2 5h20v2l-10 6L2 7zM2 9.3l10 6 10-6V19H2z"/></svg>sales@orvaflooring.com.au</li>
      <li><svg viewBox="0 0 24 24"><path d="M12 2a10 10 0 1 0 0 20 10 10 0 0 0 0-20zm6.9 6h-3a15.6 15.6 0 0 0-1.3-4A8 8 0 0 1 18.9 8zM12 4c.8 1.2 1.5 2.5 1.9 4h-3.8c.4-1.5 1.1-2.8 1.9-4zM4.3 14a8 8 0 0 1 0-4h3.4a16 16 0 0 0 0 4zm.8 2h3a15.6 15.6 0 0 0 1.3 4A8 8 0 0 1 5.1 16zm3-8h-3a8 8 0 0 1 4.3-4A15.6 15.6 0 0 0 8.1 8zM12 20c-.8-1.2-1.5-2.5-1.9-4h3.8c-.4 1.5-1.1 2.8-1.9 4zm2.3-6H9.7a14.7 14.7 0 0 1 0-4h4.6a14.7 14.7 0 0 1 0 4zm.3 6a15.6 15.6 0 0 0 1.3-4h3a8 8 0 0 1-4.3 4zm1.7-6a16 16 0 0 0 0-4h3.4a8 8 0 0 1 0 4z"/></svg>www.orvaflooring.com.au</li>
    </ul>

    <address class="address address--linfield">
      Linfield Showroom<br>462 Bramwell Hwy,<br>Linfield VIC 3218
    </address>
  </section>

  <section class="card card--back">
    <div class="wordmark">
      <span class="wordmark__dot"></span>
      <span class="wordmark__text">Orva Flooring</span>
    </div>

    <div class="services">
      <h2 class="services__heading">Our Services</h2>
      <p class="services__list">• Laminate • Hybrid • Timber • carpet and commercial flooring</p>
    </div>
  </section>
</main>
</body>
</html>
```